Dalton & Vesh Periodontics and Implant Solutions Business Card

We are a specialty dental practice- implants and periodontal surgery. We have just re-designed our logo and are building a new office and would like to re-design our business card. We are looking for something professional with a creative and artsy twist- something to stand out among the rest! Happy Designing!

I have uploaded all versions of our new logo and our current business card. We have 3 locations and 2 doctors.
Updates

Target Market(s)

55+

Industry/Entity Type

Dental

Contact Information for Business Card

Needs Names, logo, locations- professional and artsy!

Colors
0555a3
0592cd
34a7d7
3277b5
85cae6
85acd3
cee9f5
ecf7fb

Requirements
Must have
• our names:
• Gavin T. Dalton D.M.D.
• Marla P. Vesh D.M.D.
• Diplomate of the National Council of Gum Surgery
• Address locations:
• 462 N. Larkspur Avenue Suite 210B Plantation, FL 33324
• Tel: 954-603-2281 Fax: 954-603-2895
• 5174 Hollins Lane #C-3 Boca Raton, FL 33434
• Tel: 561-327-6018 Fax: 561-327-6092
• 381 Northwest 7th Street #412 Miami FL 33131
• Tel: 786-540-3316 Fax: 786-540-3389
Nice to have
• unique look
Should not have
• doesn't need QR like our current card has.

```html
<!DOCTYPE html>
<html lang="en">
<head>
<meta charset="utf-8">
<title>Dalton &amp; Vesh Business Card</title>
<link href="https://fonts.googleapis.com/css2?family=Open+Sans:wght@400;600;700&display=swap" rel="stylesheet">
<style>
  :root {
    --navy: #23408e;
    --blue: #0555a3;
    --sky: #34a7d7;
    --grey: #6f7378;
    --paper: #ffffff;
    --backdrop: #e9eef3;
  }
  html, body {
    margin: 0;
    width: 1200px;
    height: 843px;
    overflow: hidden;
    background: var(--backdrop);
    font-family: "Open Sans", Arial, sans-serif;
  }
  .sheet {
    position: relative;
    width: 1200px;
    height: 843px;
  }
  .card {
    position: absolute;
    left: 260px;
    width: 680px;
    height: 389px;
    background: var(--paper);
    box-shadow: 0 4px 14px rgba(0,0,0,.12);
    overflow: hidden;
  }
  .card--front { top: 20px; }
  .card--back { top: 434px; }

  /* Front */
  .social {
    position: absolute;
    top: 22px;
    right: 26px;
    display: flex;
    gap: 4px;
  }
  .social span {
    width: 20px;
    height: 20px;
    background: var(--blue);
    border-radius: 2px;
  }
  .brand {
    position: absolute;
    left: 70px;
    top: 120px;
    display: flex;
    align-items: center;
    gap: 22px;
  }
  .brand__mark {
    width: 130px;
    height: 130px;
    border-radius: 50%;
    border: 10px solid var(--navy);
    box-sizing: border-box;
    flex: none;
  }
  .brand__name {
    margin: 0;
    font-weight: 600;
    font-size: 46px;
    line-height: 1;
    letter-spacing: 1px;
    color: var(--navy);
    text-transform: uppercase;
  }
  .brand__tagline {
    margin: 8px 0 0;
    font-size: 19px;
    color: var(--grey);
  }

  /* Back */
  .back__band {
    position: absolute;
    top: 0;
    right: 0;
    width: 120px;
    height: 100%;
    background: var(--navy);
  }
  .back__ring {
    position: absolute;
    left: 325px;
    top: 22px;
    width: 345px;
    height: 345px;
  }
  .locations {
    position: absolute;
    left: 38px;
    top: 34px;
    margin: 0;
    padding: 0;
    list-style: none;
    font-size: 14.5px;
    line-height: 1.4;
    color: var(--grey);
  }
  .locations li { margin-bottom: 26px; }
  .locations b { color: var(--navy); font-weight: 700; }
  .doctors {
    position: absolute;
    left: 372px;
    top: 128px;
    width: 270px;
    color: var(--grey);
    font-size: 14px;
    line-height: 1.35;
  }
  .doctors__name {
    margin: 0;
    font-weight: 700;
    font-size: 19px;
    line-height: 1.25;
    color: var(--navy);
  }
  .doctors__title { margin: 6px 0 0; }
  .doctors__email { margin: 2px 0 0; }
</style>
</head>
<body>
<main class="sheet">
  <section class="card card--front" aria-label="Card front">
    <div class="social" aria-label="Social links">
      <span></span><span></span><span></span>
    </div>
    <div class="brand">
      <div class="brand__mark"></div>
      <div>
        <h1 class="brand__name">Dalton &amp; Vesh</h1>
        <p class="brand__tagline">Periodontics and Implant Solutions</p>
      </div>
    </div>
  </section>

  <section class="card card--back" aria-label="Card back">
    <div class="back__band"></div>
    <svg class="back__ring" viewBox="0 0 345 345" aria-hidden="true">
      <circle cx="172.5" cy="172.5" r="162" fill="#ffffff" stroke="#23408e" stroke-width="14"/>
      <circle cx="172.5" cy="172.5" r="150" fill="none" stroke="#23408e" stroke-width="2" opacity=".5"/>
    </svg>
    <ul class="locations">
      <li>462 N. Larkspur Avenue<br>Suite 210B, Plantation, FL 33324<br><b>P :</b> 954-603-2281 <b>• F :</b> 954-603-2895</li>
      <li>5174 Hollins Lane<br>#C-3 Boca Raton, FL 33434<br><b>P :</b> 561-327-6018 <b>• F :</b> 561-327-6092</li>
      <li>381 Northwest<br>7th Street #412 , Miami FL 33131<br><b>P :</b> 786-540-3316 <b>• F :</b> 786-540-3389</li>
    </ul>
    <div class="doctors">
      <p class="doctors__name">Gavin T. Dalton D.M.D.<br>Marla P. Vesh D.M.D.</p>
      <p class="doctors__title">Diplomate of the National Council<br>of Gum Surgery Founder</p>
      <p class="doctors__email">info@daltonvesh.com</p>
    </div>
  </section>
</main>
</body>
</html>
```